New Tech Support Service needs a website design

We need a web design for a new product we are developing that provides tech support to consumers for a small ongoing monthly fee. We are looking for a fresh, technology look and feel. We want the site to have a tech feel - yet not intimidating. Simple and welcoming. We are in need of an initial landing page, sign on page, and a product home page.

Thank you to everyone who submitted designs. It was a very difficult decision!

Tech

```html
<!DOCTYPE html>
<html lang="en">
<head>
<meta charset="utf-8">
<title>Tech Support – Landing</title>
<link rel="stylesheet" href="https://fonts.googleapis.com/css2?family=Oxygen:wght@300;400;700&family=Open+Sans:wght@400;600&family=PT+Sans:wght@400&display=swap">
<style>
  :root {
    --brand-blue: #1b74e4;
    --brand-blue-dark: #0c5fd0;
    --text-dark: #333333;
    --text-body: #666666;
    --text-muted: #888888;
    --rule: #dddddd;
    --page-bg: #ffffff;
    --band-bg: #ececec;
    --footer-bg: #2e2e2e;
    --footer-text: #ffffff;
    --hero-teal: #4f7f86;
    --hero-plum: #6e3550;
    --hero-red: #b2485a;
    --social-a: #3b5aa5;
    --social-b: #2a9fd8;
    --social-c: #f0651b;
    --social-d: #d52a27;
  }
  * { box-sizing: border-box; margin: 0; padding: 0; }
  html, body { width: 680px; height: 1200px; overflow: hidden; background: var(--page-bg); }
  body { position: relative; font-family: "Open Sans", Arial, sans-serif; color: var(--text-body); }
  h1, h2 { font-weight: 400; }
  .heading { font-family: "Oxygen", "Open Sans", sans-serif; }

  /* Header */
  .site-header { position: absolute; top: 0; left: 0; width: 680px; height: 84px; }
  .site-logo { position: absolute; left: 47px; top: 28px; font-family: "Oxygen", sans-serif; font-size: 35px; font-weight: 400; color: var(--brand-blue); letter-spacing: -0.5px; }
  .main-nav { position: absolute; right: 48px; top: 50px; display: flex; gap: 28px; }
  .main-nav a { font-family: "Oxygen", sans-serif; font-size: 10.5px; color: var(--text-dark); text-decoration: none; }

  /* Hero */
  .hero { position: absolute; top: 84px; left: 0; width: 680px; height: 273px;
    background: radial-gradient(ellipse at 20% 30%, var(--hero-teal) 0%, transparent 55%),
                radial-gradient(ellipse at 95% 90%, var(--hero-red) 0%, transparent 60%),
                linear-gradient(100deg, #5a6a78 0%, var(--hero-plum) 45%, #8a3d55 100%); }
  .hero-visual { position: absolute; left: 95px; top: 28px; width: 232px; height: 215px; border-radius: 12px;
    background: linear-gradient(160deg, #9fd3e6 0%, #3d8fb5 55%, #2a5f86 100%); opacity: 0.85; transform: skewY(8deg); }
  .hero-title { position: absolute; left: 378px; top: 80px; font-size: 21px; font-weight: 300; color: #fff; white-space: nowrap; }
  .hero-text { position: absolute; left: 379px; top: 114px; width: 230px; font-size: 9.5px; line-height: 16px; color: #f4e9ee; }
  .hero-button { position: absolute; left: 379px; top: 157px; width: 63px; height: 20px; background: #fff; border-radius: 2px;
    font-family: "Oxygen", sans-serif; font-size: 9.5px; color: #8a2f45; text-align: center; line-height: 20px; }
  .hero-arrow { position: absolute; top: 140px; width: 32px; height: 26px; }
  .hero-arrow.prev { left: 48px; }
  .hero-arrow.next { left: 600px; }

  /* Features */
  .features { position: absolute; top: 398px; left: 0; width: 680px; }
  .feature { position: absolute; width: 190px; text-align: center; }
  .feature svg { display: block; margin: 0 auto; }
  .feature-title { margin-top: 14px; font-size: 15.5px; font-weight: 400; color: var(--brand-blue); }
  .feature-text { margin-top: 6px; font-size: 8.5px; line-height: 14.5px; color: var(--text-body); white-space: nowrap; }

  .divider { position: absolute; top: 595px; left: 50px; width: 581px; height: 1px; background: var(--rule); }

  /* About */
  .about-visual { position: absolute; left: 98px; top: 652px; width: 236px; height: 176px;
    background: linear-gradient(180deg, #f4f4f4 0%, #9aa39b 40%, #7f8a86 60%, #f7f7f7 62%, #ffffff 100%);
    box-shadow: 0 1px 4px rgba(0,0,0,0.25); }
  .about-lens { position: absolute; left: 50px; top: 634px; width: 118px; height: 118px; border-radius: 50%;
    background: linear-gradient(180deg, #f6f6f6 0%, #f6f6f6 40%, #a6ad9f 41%, #8c9387 100%);
    border: 4px solid #fff; box-shadow: 0 1px 6px rgba(0,0,0,0.3); }
  .about-title { position: absolute; left: 363px; top: 656px; font-size: 18px; color: var(--text-dark); font-weight: 400; }
  .about-text { position: absolute; left: 363px; top: 684px; width: 272px; font-family: "PT Sans", "Open Sans", sans-serif;
    font-size: 8px; line-height: 11.2px; color: var(--text-muted); white-space: nowrap; }
  .about-button { position: absolute; left: 363px; top: 784px; width: 82px; height: 20px; border: 1.5px solid var(--brand-blue);
    border-radius: 10px; font-family: "Oxygen", sans-serif; font-size: 9px; color: var(--brand-blue); line-height: 17px; padding-left: 10px; }
  .about-button svg { position: absolute; right: 9px; top: 5px; }

  /* Testimonials */
  .testimonials { position: absolute; top: 879px; left: 0; width: 680px; height: 253px; }
  .testimonials-backdrop { position: absolute; inset: 0; background: linear-gradient(90deg, #e4e4e4 0%, #f0f0f0 50%, #e2e2e2 100%); }
  .testimonials-title { position: absolute; top: 24px; width: 680px; text-align: center; font-size: 18px; font-weight: 400; color: var(--text-dark); }
  .client-photo { position: absolute; left: 300px; top: 61px; width: 80px; height: 80px; border-radius: 50%;
    background: linear-gradient(180deg, #c9a98c 0%, #e8d2c0 100%); border: 3px solid #fff; box-shadow: 0 0 3px rgba(0,0,0,0.2); }
  .quote { position: absolute; top: 161px; left: 40px; width: 600px; text-align: center; font-size: 9.8px; line-height: 16px; color: var(--text-dark); }
  .quote-author { position: absolute; top: 198px; right: 78px; font-size: 9.5px; color: var(--text-dark); }
  .quote-author small { font-size: 8px; color: var(--text-body); }
  .slider-dots { position: absolute; top: 224px; left: 319px; display: flex; gap: 3px; }
  .slider-dots span { width: 8px; height: 8px; border-radius: 50%; background: #e2e2e2; border: 1px solid #aaa; }
  .slider-dots span.active { background: #777; }

  /* Footer */
  .site-footer { position: absolute; top: 1132px; left: 0; width: 680px; height: 68px; background: var(--footer-bg); font-family: Arial, sans-serif; }
  .footer-links { position: absolute; left: 61px; top: 18px; font-size: 8.5px; color: var(--footer-text); }
  .footer-copy { position: absolute; left: 61px; top: 38px; font-size: 8.5px; color: var(--footer-text); }
  .social { position: absolute; left: 512px; top: 25px; display: flex; gap: 7px; }
  .social span { width: 20px; height: 20px; }
</style>
</head>
<body>

<header class="site-header">
  <div class="site-logo">Logo</div>
  <nav class="main-nav">
    <a href="#">Home</a><a href="#">About Us</a><a href="#">Services</a><a href="#">Testimonials</a><a href="#">Contact</a>
  </nav>
</header>

<section class="hero">
  <div class="hero-visual" role="img" aria-label="Layered smartphone interface screens floating in perspective"></div>
  <h1 class="hero-title heading">Duis luctus tellus aliuam</h1>
  <p class="hero-text">Claritas est etiam processus dynamicus, qui sequi tur mutationem consuetudium lectorum.</p>
  <div class="hero-button">Read More</div>
  <svg class="hero-arrow prev" viewBox="0 0 32 26"><path d="M14 2 L3 13 L14 24 M3 13 H31" fill="none" stroke="#fff" stroke-width="1.6"/></svg>
  <svg class="hero-arrow next" viewBox="0 0 32 26"><path d="M18 2 L29 13 L18 24 M29 13 H1" fill="none" stroke="#fff" stroke-width="1.6"/></svg>
</section>

<section class="features">
  <div class="feature" style="left:51px">
    <svg width="74" height="76" viewBox="0 0 74 76">
      <path d="M30 3 Q37 -1 44 3 L66 16 Q72 20 72 27 L72 49 Q72 56 66 60 L44 73 Q37 77 30 73 L8 60 Q2 56 2 49 L2 27 Q2 20 8 16 Z" fill="var(--brand-blue)"/>
      <path d="M20 38 L54 24 L44 54 L36 44 Z M36 44 L54 24" fill="#fff" stroke="var(--brand-blue)" stroke-width="1.2" stroke-linejoin="round"/>
    </svg>
    <h2 class="feature-title heading">Services</h2>
    <p class="feature-text">Claritas est eteus dynamicuin thts,<br>qui sequitur mutatiem consuetud Claritas<br>dynamicusClaritas est etiam procss</p>
  </div>
  <div class="feature" style="left:245px">
    <svg width="74" height="76" viewBox="0 0 74 76">
      <path d="M30 3 Q37 -1 44 3 L66 16 Q72 20 72 27 L72 49 Q72 56 66 60 L44 73 Q37 77 30 73 L8 60 Q2 56 2 49 L2 27 Q2 20 8 16 Z" fill="var(--brand-blue)"/>
      <circle cx="37" cy="38" r="17" fill="none" stroke="#fff" stroke-width="5" stroke-dasharray="5 3.5"/>
      <circle cx="37" cy="38" r="11" fill="#fff"/>
      <path d="M31 33 Q35 31 37 35 Q40 38 37 42 M39 30 Q43 33 45 37" fill="none" stroke="var(--brand-blue)" stroke-width="2"/>
    </svg>
    <h2 class="feature-title heading">Technologies</h2>
    <p class="feature-text">Claritas est eteus dynamicuin thts,<br>qui sequitur mutatiem consuetud Claritas<br>dynamicusClaritas est etiam procss</p>
  </div>
  <div class="feature" style="left:436px">
    <svg width="74" height="76" viewBox="0 0 74 76">
      <path d="M30 3 Q37 -1 44 3 L66 16 Q72 20 72 27 L72 49 Q72 56 66 60 L44 73 Q37 77 30 73 L8 60 Q2 56 2 49 L2 27 Q2 20 8 16 Z" fill="var(--brand-blue)"/>
      <circle cx="37" cy="33" r="14" fill="none" stroke="#fff" stroke-width="3.5"/>
      <path d="M37 25 V34" stroke="#fff" stroke-width="3.5" stroke-linecap="round"/>
      <circle cx="37" cy="39" r="2" fill="#fff"/>
      <path d="M31 50 H43 M32 55 H42 M34 60 H40" stroke="#fff" stroke-width="3" stroke-linecap="round"/>
    </svg>
    <h2 class="feature-title heading">Consulting</h2>
    <p class="feature-text">Claritas est eteus dynamicuin thts,<br>qui sequitur mutatiem consuetud Claritas<br>dynamicusClaritas est etiam procss</p>
  </div>
</section>

<div class="divider"></div>

<section class="about">
  <div class="about-visual" role="img" aria-label="Screenshot of a product website with a building photo banner"></div>
  <div class="about-lens" role="img" aria-label="Magnified detail of the product website header"></div>
  <h2 class="about-title heading">About Our Product</h2>
  <p class="about-text">Claritas est etiam processus dynamicus, qui sequitur mutationem consuetud<br>ium lectorum. Mirum est notare quam littera gothica, quam nunc putamus pa<br>rum claram, anteposuerit litterarum formas humanitatis per.<br>Duis autem vel eum iriure dolor in hendrerit in vulputate velit esse molestie c<br>onsequat, vel illum dolore eu feugiat nulla facilisis at vero eros et accumsan e<br>t iusto odio dignissim qui blandit praesent luptatum zzril delenit.</p>
  <div class="about-button">Get Started
    <svg width="10" height="8" viewBox="0 0 10 8"><path d="M0 4 H9 M6 1 L9 4 L6 7" fill="none" stroke="var(--brand-blue)" stroke-width="1.5"/></svg>
  </div>
</section>

<section class="testimonials">
  <div class="testimonials-backdrop" role="img" aria-label="Faded grey mosaic of client portrait photos"></div>
  <h2 class="testimonials-title heading">Client Testimonials</h2>
  <div class="client-photo" role="img" aria-label="Portrait photo of the client"></div>
  <p class="quote">I am so happy to have met you! Before Vocal Reset, I had vocal<br>problems that clouded my mind and made it zero fun to sing. Now I sing again and even have a weekly job as a speaker.</p>
  <div class="quote-author">- Marco, <small>Germany</small></div>
  <div class="slider-dots"><span class="active"></span><span></span><span></span><span></span></div>
</section>

<footer class="site-footer">
  <div class="footer-links">Terms and Conditions | Privacy Promise | FAQ's | Contact Us</div>
  <div class="footer-copy">Copyright © 2013. All Rights Reserved.</div>
  <div class="social">
    <span style="background:var(--social-a)"></span>
    <span style="background:var(--social-b)"></span>
    <span style="background:var(--social-c)"></span>
    <span style="background:var(--social-d)"></span>
  </div>
</footer>

</body>
</html>
```